Letterhead to Prospective Clients

Create a letterhead (word & canva) that I will use to send letters to prospective clients and also include the Coralwood Estate Partners Logo, My Contact Details and Interchangeable "Suburb". Use the same font and colour pallete

Maris Dulworth | "Suburb" Specialist - Harrowvale & Surrounds
Mobile: 0417 862 095
Email: MD@CoralwoodEstatePartners.com.au

```html
<!DOCTYPE html>
<html lang="en">
<head>
<meta charset="utf-8">
<title>Coralwood Estate Partners Letterhead</title>
<link rel="stylesheet" href="https://fonts.googleapis.com/css2?family=Montserrat:wght@300;400;700&family=Arimo:wght@400&display=swap">
<style>
  :root {
    --navy: #1b2e4b;
    --gold: #d6a96b;
    --rule: #9a9a9a;
    --ink: #111111;
    --paper: #ffffff;
    --backdrop: #e6e6e6;
  }
  * { margin: 0; padding: 0; box-sizing: border-box; }
  html, body { width: 1200px; height: 960px; overflow: hidden; }
  body {
    background: var(--backdrop);
    display: flex;
    align-items: center;
    justify-content: center;
  }
  .letterhead {
    position: relative;
    width: 640px;
    height: 905px;
    background: var(--paper);
    box-shadow: 0 2px 10px rgba(0,0,0,0.12);
    overflow: hidden;
  }
  .masthead {
    position: absolute;
    left: 48px;
    right: 48px;
    top: 58px;
    display: flex;
    align-items: center;
  }
  .brand-name {
    font-family: "Montserrat", sans-serif;
    font-weight: 300;
    color: var(--navy);
    font-size: 25px;
    line-height: 1.15;
    letter-spacing: 0.06em;
    text-transform: uppercase;
    width: 270px;
  }
  .masthead-divider {
    width: 1px;
    height: 66px;
    background: var(--rule);
    margin: 0 16px 0 14px;
  }
  .contact {
    font-family: "Montserrat", sans-serif;
    color: var(--navy);
    font-size: 10.5px;
    line-height: 1.55;
    font-weight: 300;
  }
  .contact-name { font-weight: 700; font-size: 11px; }
  .contact-line { display: flex; align-items: center; gap: 6px; }
  .contact-line svg { width: 10px; height: 10px; flex: none; }
  .header-rule {
    position: absolute;
    left: 48px;
    right: 48px;
    top: 152px;
    height: 1px;
    background: var(--rule);
  }
  .letter-body {
    position: absolute;
    left: 96px;
    right: 60px;
    top: 230px;
    font-family: "Arimo", sans-serif;
    color: var(--ink);
    font-size: 12px;
    line-height: 1.32;
  }
  .letter-body p { margin-bottom: 38px; }
  .footer-bands {
    position: absolute;
    left: 0;
    bottom: 0;
    width: 640px;
    height: 20px;
  }
</style>
</head>
<body>
  <main class="letterhead">
    <header class="masthead">
      <div class="brand-name">Coralwood Estate Partners</div>
      <div class="masthead-divider"></div>
      <div class="contact">
        <div class="contact-name">Maris Dulworth</div>
        <div>"Suburb" Specialist - Harrowvale &amp; Surrounds</div>
        <div class="contact-line">
          <svg viewBox="0 0 10 10" aria-hidden="true"><circle cx="5" cy="5" r="5" fill="var(--navy)"/><path d="M3.2 2.6c.3-.2.6-.1.8.2l.4.7c.1.3 0 .5-.2.6l-.3.2c.3.7.8 1.2 1.5 1.5l.2-.3c.1-.2.4-.3.6-.2l.7.4c.3.2.4.5.2.8-.3.5-.8.7-1.4.5C4.4 6.7 3.3 5.6 2.8 4.3c-.2-.6 0-1.2.4-1.7z" fill="#fff"/></svg>
          <span>0417 862 095</span>
        </div>
        <div class="contact-line">
          <svg viewBox="0 0 10 10" aria-hidden="true"><rect x="0.5" y="2" width="9" height="6.5" fill="var(--navy)"/><path d="M0.8 2.3 5 5.6 9.2 2.3" fill="none" stroke="#fff" stroke-width="0.8"/></svg>
          <span>MD@CoralwoodEstatePartners.com.au</span>
        </div>
      </div>
    </header>
    <div class="header-rule"></div>

    <section class="letter-body">
      <p>Lorem ipsum dolor sit amet, consectetur adipiscing elit. Donec fringilla neque euismod volutpat cursus. Vestibulum ac pretium orci, consequat elementum velit. Etiam bibendum purus ac augue finibus volutpat. Vestibulum justo nisl.</p>
      <p>Lorem ipsum dolor sit amet, consectetur adipiscing elit. Donec fringilla neque euismod volutpat cursus. Vestibulum ac pretium orci, consequat elementum velit. Etiam bibendum purus ac augue finibus volutpat. Vestibulum justo nisl, gravida aliquet sollicitudin ut, finibus vitae mi. Praesent aliquet scelerisque blandit. Sed id varius lacus, id tristique sem. Fusce et lobortis leo. Aliquam mollis pellentesque magna, condimentum ullamcorper ex ullamcorper non. Morbi ultricies nunc eu tellus dignissim, eget venenatis dolor ullamcorper. Etiam dolor eros, iaculis at ultricies nec, volutpat nec orci. Vivamus tincidunt rutrum sapien, ac porttitor mauris tristique nec.</p>
      <p>Lorem ipsum dolor sit amet, consectetur adipiscing elit. Donec fringilla neque euismod volutpat cursus. Vestibulum ac pretium orci, consequat elementum velit. Etiam bibendum purus ac augue finibus volutpat. Vestibulum justo nisl, gravida aliquet sollicitudin ut, finibus vitae mi. Praesent aliquet scelerisque blandit. Sed id varius lacus, id tristique sem. Fusce et lobortis leo. Aliquam mollis pellentesque magna, condimentum ullamcorper ex ullamcorper non. Morbi ultricies nunc eu tellus dignissim, eget venenatis dolor ullamcorper. Etiam dolor eros, iaculis at ultricies nec, volutpat nec orci. Vivamus tincidunt rutrum sapien, ac porttitor mauris tristique nec.</p>
      <p>Lorem ipsum dolor sit amet, consectetur adipiscing elit. Donec fringilla neque euismod volutpat cursus. Vestibulum ac pretium orci, consequat elementum velit. Etiam bibendum purus ac augue finibus volutpat. Vestibulum justo nisl.</p>
    </section>

    <svg class="footer-bands" viewBox="0 0 640 20" preserveAspectRatio="none" aria-hidden="true">
      <polygon points="0,12 352,12 346,20 0,20" fill="var(--gold)"/>
      <polygon points="360,4 640,4 640,20 348,20" fill="var(--navy)"/>
    </svg>
  </main>
</body>
</html>
```